Website design for an events management company

What we need is the design of a website to be used by an events management company, the company is called "Vanto Events Management" and the website is expected to contain the following sections:
1) Homepage
2) Who are we?
3) Mission / Vision / Core values
4) Why to choose Vanto?
5) Past experience
6) Duties or provided services (Scientific Program Duties, Accreditation, Fund Raising, Accommodations, Social Activities, Transportation, Marketing of the Event, Publications and printed materials, Secretarial Work and Media Coverage)
7) References
8) Contact Us page (will probably contain a contact us form plus email, address and a google map)

Attached for your reference the company's logo

Expected that the winner should deliver the designs of at least two pages (the homepage plus an inner page) plus of course all the used graphics, images ... etc.

Thanks

Target Market(s)

The design need to target scientific events and not public events, for example the company doesn't organize music concerts ... etc., it organizes only scientific events so please target business users (i.e. doctors, engineers, scientisits ... etc) while making the designs, including the correct colors, images and icons

Industry/Entity Type

It Company

Number of Pages Required

2 page

Requirements
Must have
• One homepage
• One inner page
• All the used graphics and images
Nice to have
• More than two pages

```html
<!DOCTYPE html>
<html lang="en">
<head>
<meta charset="utf-8">
<title>Vanto Events Management</title>
<link href="https://fonts.googleapis.com/css2?family=Raleway:wght@300;400;500;600;700&display=swap" rel="stylesheet">
<style>
:root{
  --orange:#f7941d;
  --orange-dark:#e8820c;
  --ink:#333333;
  --muted:#777777;
  --light:#f3f3f3;
  --dark:#2a2a2a;
  --darker:#1e1e1e;
  --white:#ffffff;
  --line:#dddddd;
}
*{box-sizing:border-box;margin:0;padding:0}
html,body{width:1200px;height:3409px;overflow:hidden}
body{position:relative;font-family:"Raleway",Arial,sans-serif;color:var(--ink);background:var(--white)}
section,header,footer{position:absolute;left:0;width:1200px}

/* nav + hero */
.site-nav{top:0;height:57px;background:var(--white);z-index:2;display:flex;justify-content:space-between;align-items:center;padding:0 108px 0 102px;font-size:17px;color:#444}
.site-nav a{color:inherit;text-decoration:none}
.site-nav .active{color:var(--orange)}
.hero{top:0;height:659px;background:linear-gradient(180deg,#e9e9ea 0%,#dcdcdc 45%,#7d7f84 62%,#3e4046 100%)}
.hero-screen{position:absolute;left:64px;top:57px;width:1072px;height:313px;background:linear-gradient(180deg,#ffffff,#f1f1f1)}
.hero-brand{position:absolute;left:0;right:0;top:100px;text-align:center}
.hero-brand .mark{display:inline-block;width:46px;height:46px;border-radius:50%;background:var(--orange);vertical-align:middle;margin-right:12px}
.hero-brand .name{font-size:64px;font-weight:700;color:#444;vertical-align:middle}
.hero-brand .tag{display:block;font-size:17px;color:#555;margin-top:2px}
.hero-dots{position:absolute;top:633px;left:0;right:0;text-align:center}
.hero-dots span{display:inline-block;width:15px;height:15px;border:2px solid #555;border-radius:50%;margin:0 8px;background:var(--white)}
.hero-dots span.on{background:#555;box-shadow:inset 0 0 0 3px #fff}

.section-title{text-align:center;font-weight:600;color:var(--orange)}
.section-sub{text-align:center;color:#555}

/* intro */
.intro{top:659px;height:182px}
.intro h1{margin-top:48px;font-size:40px;font-weight:700}
.intro p{font-size:20px;margin-top:8px}

/* services */
.services{top:841px;height:598px;background:linear-gradient(180deg,#4a4a4a,#2f2f2f 70%,#3a3a3a)}
.service{position:absolute;top:70px;width:250px;text-align:center;color:var(--white)}
.service .icon{width:86px;height:86px;border-radius:50%;background:#e6e6e6;margin:0 auto;display:flex;align-items:center;justify-content:center}
.service.featured .icon{background:var(--orange);box-shadow:0 0 0 5px #3a3a3a,0 0 0 8px var(--orange)}
.service h3{font-size:22px;font-weight:700;margin-top:26px;line-height:28px}
.service .lead{font-size:14px;margin-top:4px;line-height:18px}
.service .body{font-size:14px;line-height:22px;margin-top:26px;height:146px;overflow:hidden}
.btn{display:inline-block;font-size:13px;text-transform:uppercase;padding:0 18px;height:42px;line-height:40px;border:2px solid #ddd;color:var(--white)}
.btn.fill{background:var(--orange);border-color:var(--orange)}
.pager{position:absolute;left:0;right:0;text-align:center;font-size:0}
.pager span{display:inline-block;vertical-align:middle;height:42px;line-height:40px;border:1px solid #ccc;background:var(--white);color:#555;font-size:13px;margin:0 12px}
.pager .arrow{width:40px;font-size:18px}
.pager .arrow.hot{background:var(--orange);border-color:var(--orange);color:var(--white)}
.pager .label{padding:0 16px;text-transform:uppercase}

/* cta */
.cta{top:1439px;height:261px;background:var(--darker);text-align:center;color:var(--white)}
.cta h2{margin-top:58px;font-size:40px;font-weight:400;color:var(--orange)}
.cta h2 b{font-weight:700}
.cta p{font-size:16px;margin-top:12px}
.cta .btn{margin-top:24px;height:42px;padding:0 32px;font-size:13px}

/* work */
.work{top:1700px;height:562px;background:var(--white)}
.work h2{margin-top:44px;font-size:40px;font-weight:400}
.work .section-sub{font-size:16px;margin-top:6px}
.work-grid{position:absolute;top:146px;left:0;display:flex;width:1200px}
.work-card{width:300px;height:279px;background:var(--light);text-align:center}
.work-card.current{background:var(--white);border-bottom:2px solid var(--line)}
.work-photo{height:166px;position:relative}
.work-card h4{font-size:17px;font-weight:700;margin-top:20px;color:#222}
.work-card p{font-size:14px;color:var(--muted);line-height:23px;margin-top:6px}
.work-actions{position:absolute;top:50%;left:50%;transform:translate(-50%,-50%);display:flex;gap:14px}
.work-actions span{width:42px;height:42px;border-radius:50%;display:flex;align-items:center;justify-content:center}

/* values */
.values{top:2262px;height:563px;background:linear-gradient(120deg,#2c2c2c,#4b4b4b 55%,#2a2a2a)}
.values h2{margin-top:52px;text-align:center;color:var(--white);font-size:40px;font-weight:400}
.values h2 b{color:var(--orange);font-weight:700}
.value{position:absolute;display:flex;align-items:center;color:var(--white);font-size:18px}
.value i{width:30px;height:30px;border-radius:50%;border:3px solid #888;background:#2c2c2c;display:flex;align-items:center;justify-content:center;margin-right:6px}
.value i::after{content:"";width:12px;height:12px;border-radius:50%;background:currentColor}

/* clients */
.clients{top:2825px;height:314px;background:var(--light)}
.clients h2{margin-top:48px;font-size:40px;font-weight:400}
.clients .section-sub{font-size:16px;margin-top:6px}
.client{position:absolute;top:195px;transform:translateX(-50%);font-size:22px;font-weight:700;color:#555;display:flex;align-items:center;gap:8px;white-space:nowrap}
.client i{width:14px;height:14px;border-radius:50%;background:#888;display:inline-block}
.client-arrow{position:absolute;top:188px;width:38px;height:44px;border:1px solid #ccc;background:var(--white);display:flex;align-items:center;justify-content:center;color:#555}
.client-arrow.hot{border-color:var(--orange);color:var(--orange)}

/* footer */
.site-footer{top:3139px;height:221px;background:#1f1f1f;color:#ccc}
.foot-col{position:absolute;top:30px}
.foot-col h5{font-size:20px;font-weight:400;color:var(--white)}
.foot-col p{font-size:14px;line-height:23px;margin-top:8px}
.social{display:flex;gap:18px;margin-top:20px;align-items:center}
.social i{width:14px;height:14px;border-radius:50%;background:#888;display:inline-block}
.social .box{width:42px;height:42px;border:1px solid var(--orange);display:flex;align-items:center;justify-content:center}
.social .box i{background:var(--orange)}
.tweet{display:flex;gap:14px;margin-top:14px;font-size:14px;line-height:22px;width:310px}
.tweet .bird{width:22px;height:22px;border-radius:50%;background:#888;flex:none;margin-top:4px}
.tweet b{color:var(--orange);font-weight:400}
.tweet em{font-style:italic;color:#999;float:right}
.subscribe-form{display:flex;margin-top:16px;width:332px;height:55px}
.subscribe-form .field{flex:1;background:var(--white);color:#aaa;font-style:italic;font-size:14px;display:flex;align-items:center;padding-left:22px}
.subscribe-form .go{width:96px;background:var(--orange);color:var(--white);font-weight:700;font-size:15px;display:flex;align-items:center;justify-content:center}
.copyright{position:absolute;top:3360px;height:49px;left:0;width:1200px;background:#151515;color:#ccc;font-size:14px;text-align:center;line-height:49px}
.copyright b{color:var(--orange);font-weight:600}
.to-top{position:absolute;right:18px;top:14px;width:36px;height:35px;background:var(--white);display:flex;align-items:center;justify-content:center}
</style>
</head>
<body>

<header class="site-nav">
  <a class="active">Home</a><a>Who are we?</a><a>Mission</a><a>Why to choose Vanto?</a><a>Past experience</a><a>Duties</a><a>References</a><a>Contact Us</a>
</header>

<section class="hero" role="img" aria-label="Speaker presenting to a seated conference audience">
  <div class="hero-screen">
    <div class="hero-brand">
      <span class="mark"></span><span class="name">Vanto</span>
      <span class="tag">Vanto Events Management</span>
    </div>
  </div>
  <div class="hero-dots"><span class="on"></span><span></span><span></span><span></span></div>
</section>

<section class="intro">
  <h1 class="section-title">Be Positive … Be Creative</h1>
  <p class="section-sub">Top reasons to work with us</p>
</section>

<section class="services" aria-label="Services">
  <div class="service featured" style="left:80px">
    <div class="icon"><svg width="46" height="46" viewBox="0 0 46 46" fill="none" stroke="#fff" stroke-width="2"><ellipse cx="23" cy="23" rx="20" ry="8"/><ellipse cx="23" cy="23" rx="20" ry="8" transform="rotate(60 23 23)"/><ellipse cx="23" cy="23" rx="20" ry="8" transform="rotate(-60 23 23)"/><circle cx="23" cy="23" r="3" fill="#fff"/></svg></div>
    <h3>Scientific Program</h3>
    <p class="lead">Lorem Ipsum is simply dummy text.</p>
    <p class="body">Performing all tasks according to a clear time frame.<br>Preparation of the data of the first &amp; the second announcements in innovative designs.</p>
    <span class="btn fill">Read more</span>
  </div>
  <div class="service" style="left:343px">
    <div class="icon"><svg width="40" height="44" viewBox="0 0 40 44" fill="none" stroke="#555" stroke-width="2.5"><path d="M6 3h20l8 8v30H6z"/><path d="M12 16h16M12 22h16M12 28h10"/></svg></div>
    <h3>Accreditation</h3>
    <p class="lead">Lorem Ipsum is simply dummy text.</p>
    <p class="body">Preparation of the application forms needed by the accreditation boards (Egyptian, Arab, European or American) after fulfilling their prerequisites.</p>
    <span class="btn">Read more</span>
  </div>
  <div class="service" style="left:607px">
    <div class="icon"><svg width="42" height="42" viewBox="0 0 42 42" fill="none" stroke="#555" stroke-width="2.5"><circle cx="21" cy="15" r="9"/><path d="M21 10v10M18 12h5a2 2 0 010 4h-4a2 2 0 000 4h5"/><path d="M4 30l8 8h18l8-8"/></svg></div>
    <h3>Fund Raising</h3>
    <p class="lead">Lorem Ipsum is simply dummy text.</p>
    <p class="body">Preparing the preliminary event budget.<br>Tailoring several attractive benefits packages to suite the target sponsors.</p>
    <span class="btn">Read more</span>
  </div>
  <div class="service" style="left:871px">
    <div class="icon"><svg width="48" height="34" viewBox="0 0 48 34" fill="#555"><rect x="2" y="8" width="24" height="18" rx="4"/><rect x="22" y="12" width="24" height="16" rx="4"/><circle cx="9" cy="29" r="4"/><circle cx="38" cy="30" r="4"/></svg></div>
    <h3>Transportation</h3>
    <p class="lead">Lorem Ipsum is simply dummy text.</p>
    <p class="body">Shuttle buses from different hotels or meeting points.<br>Flight tickets reservation for guest faculty.</p>
    <span class="btn">Read more</span>
  </div>
  <div class="pager" style="top:493px"><span class="arrow">‹</span><span class="label">See all services</span><span class="arrow hot">›</span></div>
</section>

<section class="cta">
  <h2>Want To <b>Work</b> with Us ?</h2>
  <p>Nothing is impossible ….. even the word itself says I'm possible.</p>
  <span class="btn fill">Get started</span>
</section>

<section class="work">
  <h2 class="section-title">Our Latest Work</h2>
  <p class="section-sub">Lorem Ipsum is simply dummy text of the printing</p>
  <div class="work-grid">
    <div class="work-card current">
      <div class="work-photo" role="img" aria-label="Empty conference hall set for an event" style="background:linear-gradient(180deg,#d8d8d8,#f2f2f2)">
        <div class="work-actions"><span style="background:#666"><svg width="18" height="18" viewBox="0 0 18 18" fill="none" stroke="#fff" stroke-width="2"><circle cx="7.5" cy="7.5" r="5.5"/><path d="M12 12l5 5"/></svg></span><span style="background:var(--orange)"><svg width="18" height="18" viewBox="0 0 18 18" fill="none" stroke="#fff" stroke-width="2"><rect x="2" y="6" width="8" height="5" rx="2.5" transform="rotate(-45 6 8.5)"/><rect x="8" y="7" width="8" height="5" rx="2.5" transform="rotate(-45 12 9.5)"/></svg></span></div>
      </div>
      <h4>Thrombosis &amp; Hemostasis</h4>
      <p>The 16th Annual Conference of the<br>Working Group of</p>
    </div>
    <div class="work-card">
      <div class="work-photo" role="img" aria-label="Audience attending a conference session" style="background:linear-gradient(180deg,#c7a6b0,#3d3a40)"></div>
      <h4>Thrombosis &amp; Hemostasis</h4>
      <p>The 16th Annual Conference of the<br>Working Group of</p>
    </div>
    <div class="work-card">
      <div class="work-photo" role="img" aria-label="Business team meeting around a table" style="background:linear-gradient(180deg,#dfe3e6,#9aa0a6)"></div>
      <h4>Thrombosis &amp; Hemostasis</h4>
      <p>The 16th Annual Conference of the<br>Working Group of</p>
    </div>
    <div class="work-card">
      <div class="work-photo" role="img" aria-label="Delegates applauding at an event" style="background:linear-gradient(180deg,#e6ded6,#a28a78)"></div>
      <h4>Thrombosis &amp; Hemostasis</h4>
      <p>The 16th Annual Conference of the<br>Working Group of</p>
    </div>
  </div>
  <div class="pager" style="top:467px"><span class="arrow">‹</span><span class="label">See all work</span><span class="arrow">›</span></div>
</section>

<section class="values" role="img" aria-label="Notebook and pen on a desk" >
  <h2>Core Values <b>“WE RESPECT”</b></h2>
  <div class="value" style="left:125px;top:134px"><i style="color:#888"></i><span><span style="color:#888">W</span>e use our platform as business leaders to draw attention to society causes.</span></div>
  <div class="value" style="left:166px;top:176px"><i style="color:#9b2d9b"></i><span><span style="color:#9b2d9b">E</span>stablishing long-term relations with our customers.</span></div>
  <div class="value" style="left:207px;top:218px"><i style="color:#7a2b8f"></i><span><span style="color:#7a2b8f">R</span>esponsibility towards the community.</span></div>
  <div class="value" style="left:248px;top:260px"><i style="color:#29a8e0"></i><span><span style="color:#29a8e0">E</span>stablishing a Life-long Learning.</span></div>
  <div class="value" style="left:289px;top:302px"><i style="color:#f2c318"></i><span><span style="color:#f2c318">S</span>urpassing obstacles.</span></div>
  <div class="value" style="left:330px;top:344px"><i style="color:#8dc63f"></i><span><span style="color:#8dc63f">P</span>ositive ambition.</span></div>
  <div class="value" style="left:371px;top:386px"><i style="color:#f7941d"></i><span><span style="color:#f7941d">E</span>agerness to innovate.</span></div>
  <div class="value" style="left:412px;top:428px"><i style="color:#e3262e"></i><span><span style="color:#e3262e">C</span>ustomer Satisfaction.</span></div>
  <div class="value" style="left:453px;top:470px"><i style="color:#888"></i><span><span style="color:#888">T</span>aking a leadership role in shaping the event management industry.</span></div>
</section>

<section class="clients">
  <h2 class="section-title">Our Prestigious Clients</h2>
  <p class="section-sub">Lorem Ipsum is simply dummy text of the printing</p>
  <span class="client-arrow" style="left:15px">‹</span>
  <div class="client" style="left:175px"><i></i>Northgate</div>
  <div class="client" style="left:350px">Coretel</div>
  <div class="client" style="left:525px">Halvorsen</div>
  <div class="client" style="left:700px">Quellan</div>
  <div class="client" style="left:875px">Pylora</div>
  <div class="client" style="left:1045px">Brightmere</div>
  <span class="client-arrow hot" style="left:1145px">›</span>
</section>

<footer class="site-footer">
  <div class="foot-col" style="left:80px;width:320px">
    <h5>About</h5>
    <p>Lorem Ipsum is simply dummy text of the printing and typesetting industry. Lorem Ipsum has been the industry's standard dummy text ever since the 1500s.</p>
    <div class="social"><span class="box"><i></i></span><i></i><i></i><i></i><i></i><i></i></div>
  </div>
  <div class="foot-col" style="left:436px">
    <h5>Recent Tweets</h5>
    <div class="tweet"><span class="bird"></span><span><b>@Dana Reyes</b> I belive that. Lorem Ipsum is simply dummy text of the printing and typesetting industry. <em>4 days ago</em></span></div>
    <div class="tweet"><span class="bird"></span><span><b>@Market Owl</b> Check this stock chart. This price is crazy! <em>4 days ago</em></span></div>
  </div>
  <div class="foot-col" style="left:791px">
    <h5>Subscribe</h5>
    <p style="width:330px">Sign up to get updates about innovative and extra utility new products developed by Lumora Web Developers.</p>
    <div class="subscribe-form"><span class="field">Enter E-Mail Address</span><span class="go">SIGN UP</span></div>
  </div>
</footer>
<div class="copyright">© <b>Vanto Events Management</b> - 2015, All Rights Reserved.
  <span class="to-top"><svg width="12" height="8" viewBox="0 0 12 8" fill="none" stroke="#f7941d" stroke-width="2"><path d="M1 7l5-5 5 5"/></svg></span>
</div>

</body>
</html>
```